Logo/Stationary for Personal Injury Law Firm

We need a logo for our firm and stationary (letterhead, business cards, envelopes) to feature it. We are a personal injury firm that is branching off and starting on our own. Our firm name is "Halvorsen Law, P.C." We would like to take a more modern approach with the design, but still look professional. Our firm takes a very personal approach with all of our clients.
Updates
Here is the info located in the supported file (if you couldnt access it): 4127 North Birchwood Lane Oklahoma City, Oklahoma 73482 Telephone: (405) 362-8140 Fax: (405) 362-8177 Toll Free: (866) 362-8140 Website: www.HalvorsenLaw.example Email: name@halvorsenlaw.example Attorneys: Garrett Halvorsen – licensed to practice in Oklahoma Dustin Pellow – licensed to practice in Oklahoma Of Counsel Cyrus Ponder – licensed to practice in Texas Stefan Ruokola – licensed to practice in New York
Halvorsen Law, P.C.
I have attached an example of the letterhead from our old firm. The main attorneys (Garrett & Dustin) should come first and the of counsel attorneys should be second because they just assist with cases. But please don't let this example box you in to a certain concept.
Target Market(s)
Potential clients involved in personal injury cases (auto accidents, pharmaceutical litigation, medical malpractice & nursing home negligence).
Industry/Entity Type
Lawyer
Requirements
Must have
- Logo - Firm name "Halvorsen Law, P.C."
- Letterhead - Please see the supporting file containing all the information that needs to be presented.
- Business Card - name, title (attorney/legal assistant), address, telephone, fax, email, website
- Envelope - Logo and address
Should not have
- All of the attorneys are male, so we aren''t interested in any feminine designs.
- Please do not use any scales, gavels or family crest designs.

```html
<!DOCTYPE html>
<html lang="en">
<head>
<meta charset="utf-8">
<title>Halvorsen Law, P.C. — Stationery</title>
<link href="https://fonts.googleapis.com/css2?family=EB+Garamond:wght@400;500;700&display=swap" rel="stylesheet">
<style>
  :root {
    --ink: #111111;
    --navy: #0a1a8c;
    --royal: #1a33d6;
    --deep: #00106a;
    --paper: #ffffff;
    --rule: #1a1a1a;
  }
  * { margin: 0; padding: 0; box-sizing: border-box; }
  html, body { width: 1200px; height: 803px; overflow: hidden; background: var(--paper); }
  body { position: relative; font-family: "EB Garamond", Garamond, serif; color: var(--ink); }
  .sheet { position: absolute; background: var(--paper); border: 1px solid var(--rule); }

  /* brand wordmark */
  .brand { position: absolute; display: flex; align-items: center; gap: 0.35em; font-weight: 700; font-variant: small-caps; line-height: 0.92; color: var(--ink); }
  .brand .mark { display: block; width: 0.7em; height: 0.7em; background: var(--navy); flex: none; }
  .brand--light { color: var(--paper); }
  .brand--light .mark { background: var(--paper); }

  /* letterhead */
  .letterhead { left: 0; top: 0; width: 621px; height: 803px; }
  .letterhead .brand { left: 47px; top: 50px; font-size: 31px; }
  .letterhead__address { position: absolute; right: 46px; top: 51px; text-align: right; font-size: 11px; line-height: 13.5px; }
  .letterhead__contact { position: absolute; right: 46px; top: 88px; text-align: right; font-size: 8.6px; line-height: 11px; }
  .roster { position: absolute; left: 47px; top: 726px; width: 540px; font-size: 10.2px; line-height: 11.5px; }
  .roster__label { position: absolute; top: 0; }
  .roster__member { position: absolute; top: 18px; white-space: nowrap; }
  .roster__name { font-weight: 700; }

  /* business cards */
  .card { width: 256px; height: 146px; }
  .card--front { left: 655px; top: 54px; border: none; background: radial-gradient(ellipse at 45% 35%, #2a4bff 0%, #0a22c8 40%, var(--deep) 100%); }
  .card--front .brand { left: 37px; top: 54px; font-size: 19px; }
  .card--back { left: 944px; top: 53px; }
  .card--back .brand { left: 124px; top: 18px; font-size: 10.5px; }
  .card__person { position: absolute; left: 20px; top: 51px; }
  .card__name { color: var(--navy); font-weight: 700; font-size: 10.6px; }
  .card__title { font-size: 9px; }
  .card__info { position: absolute; left: 124px; top: 52px; font-size: 7.6px; line-height: 10.5px; }
  .card__info .addr { font-weight: 500; }
  .card__phones { margin-top: 5px; display: grid; grid-template-columns: 46px auto; font-size: 7px; line-height: 9.8px; }
  .card__phones dt { font-weight: 700; }
  .card__web { margin-top: 4px; font-size: 7px; line-height: 9.6px; }

  /* envelope */
  .envelope { left: 503px; top: 269px; width: 694px; height: 301px; }
  .envelope .brand { left: 29px; top: 26px; font-size: 22px; }
  .envelope__address { position: absolute; left: 29px; top: 77px; font-size: 10.4px; line-height: 16px; letter-spacing: 0.07em; font-weight: 500; }

  /* standalone logo */
  .brand--hero { left: 694px; top: 638px; font-size: 50px; }
</style>
</head>
<body>

  <section class="sheet letterhead" aria-label="Letterhead">
    <div class="brand"><span>Halvorsen<br>Law, P.C.</span><span class="mark"></span></div>
    <address class="letterhead__address" style="font-style:normal">4127 North Birchwood Lane<br>Oklahoma City, Oklahoma 73482</address>
    <div class="letterhead__contact">
      Telephone: (405) 362-8140<br>
      Fax: (405) 362-8177<br>
      Toll Free: (866) 362-8140<br>
      Website: www.HalvorsenLaw.example<br>
      Email: name@halvorsenlaw.example
    </div>
    <div class="roster">
      <div class="roster__label" style="left:0">Attorneys:</div>
      <div class="roster__label" style="left:283px">Of Counsel:</div>
      <div class="roster__member" style="left:0"><div class="roster__name">Garrett Halvorsen</div>licensed to practice in Oklahoma</div>
      <div class="roster__member" style="left:142px"><div class="roster__name">Dustin Pellow</div>licensed to practice in Oklahoma</div>
      <div class="roster__member" style="left:283px"><div class="roster__name">Cyrus Ponder</div>licensed to practice in Texas</div>
      <div class="roster__member" style="left:404px"><div class="roster__name">Stefan Ruokola</div>licensed to practice in New York</div>
    </div>
  </section>

  <section class="sheet card card--front" aria-label="Business card front">
    <div class="brand brand--light"><span>Halvorsen<br>Law, P.C.</span><span class="mark"></span></div>
  </section>

  <section class="sheet card card--back" aria-label="Business card back">
    <div class="brand"><span>Halvorsen<br>Law, P.C.</span><span class="mark"></span></div>
    <div class="card__person">
      <div class="card__name">Garrett Halvorsen</div>
      <div class="card__title">Attorney</div>
    </div>
    <div class="card__info">
      <div class="addr">4127 North Birchwood Lane<br>Oklahoma City, OK 73482</div>
      <dl class="card__phones">
        <dt>Tel:</dt><dd>(405) 362-8140</dd>
        <dt>Fax:</dt><dd>(405) 362-8177</dd>
        <dt>Toll Free:</dt><dd>(866) 362-8140</dd>
      </dl>
      <div class="card__web">www.HalvorsenLaw.example<br>GarrettHalvorsen@halvorsenlaw.example</div>
    </div>
  </section>

  <section class="sheet envelope" aria-label="Envelope">
    <div class="brand"><span>Halvorsen<br>Law, P.C.</span><span class="mark"></span></div>
    <div class="envelope__address">4127 North Birchwood Lane<br>Oklahoma City, Oklahoma 73482</div>
  </section>

  <div class="brand brand--hero"><span>Halvorsen<br>Law, P.C.</span><span class="mark"></span></div>

</body>
</html>
```